Design a BOLD Ad Design for Fitness Club

We are fitness facility that is about to run our new "Bright Parent Reboot" program and we need a bold design created for an ad that will run on Instagram and Facebook.

The ad needs to be eye catching, easy to read and attractive so that someone stops scrolling and clicks to join.

The add needs to be sized to 1080 x 1080, include our logo and the text "Bright Parent Reboot" and "Starting September 23rd"

I have included an example photo, which is to be used as an example only of a design style that stands out to us, (colors, female photo style, etc)

I have also included our logo, which the yellow color can be changed for this design.

Thank you and we look forward to seeing your design.

```html
<!DOCTYPE html>
<html lang="en">
<head>
<meta charset="utf-8">
<title>PulseForge – Bright Parent Reboot</title>
<link rel="stylesheet" href="https://fonts.googleapis.com/css2?family=Barlow+Condensed:ital,wght@0,700;0,800;1,700;1,800;1,900&family=Barlow:wght@700&display=swap">
<style>
  :root {
    --ink: #0b0b0b;
    --ink-soft: #1a1a1a;
    --sun: #f6c90e;
    --sun-deep: #d99a00;
    --white: #ffffff;
    --silver: #d9d9d9;
  }
  html, body {
    margin: 0;
    padding: 0;
    width: 1200px;
    height: 1200px;
    overflow: hidden;
    background: var(--ink);
  }
  .ad {
    position: relative;
    width: 1200px;
    height: 1200px;
    overflow: hidden;
    background: radial-gradient(circle at 75% 45%, var(--ink-soft), var(--ink) 70%);
    font-family: "Barlow Condensed", "Arial Narrow", sans-serif;
  }
  .ad__photo {
    position: absolute;
    inset: 0;
    width: 1200px;
    height: 1200px;
  }
  .brand {
    position: absolute;
    top: 84px;
    left: 620px;
    width: 500px;
    text-align: center;
  }
  .brand__name {
    display: block;
    font-weight: 800;
    font-size: 104px;
    line-height: 1;
    letter-spacing: 1px;
    color: var(--sun);
  }
  .brand__tagline {
    display: flex;
    align-items: center;
    justify-content: center;
    gap: 12px;
    margin-top: 12px;
    white-space: nowrap;
    font-family: "Barlow", Arial, sans-serif;
    font-weight: 700;
    font-size: 16px;
    letter-spacing: 2.5px;
    color: var(--sun);
  }
  .brand__rule {
    display: block;
    width: 30px;
    height: 2px;
    background: var(--silver);
  }
  .headline {
    position: absolute;
    top: 340px;
    left: 450px;
    width: 660px;
    margin: 0;
    text-align: center;
    transform: rotate(-4deg);
    font-weight: 900;
    font-style: italic;
    font-size: 184px;
    line-height: 0.8;
    letter-spacing: 3px;
    text-transform: uppercase;
    color: var(--white);
    text-shadow: 5px 6px 0 #6d6d6d, 10px 12px 14px rgba(0,0,0,0.7);
  }
  .headline__line { display: block; }
  .launch {
    position: absolute;
    top: 880px;
    left: 362px;
    width: 780px;
    text-align: center;
  }
  .launch__label {
    display: block;
    margin-left: -60px;
    font-style: italic;
    font-weight: 700;
    font-size: 50px;
    letter-spacing: 4px;
    color: var(--white);
  }
  .launch__row {
    display: flex;
    align-items: center;
    justify-content: space-between;
    margin-top: -2px;
  }
  .launch__date {
    font-style: italic;
    font-weight: 900;
    font-size: 82px;
    line-height: 1;
    color: var(--sun);
    white-space: nowrap;
  }
  .launch__date sup {
    margin-left: 8px;
    font-size: 36px;
    vertical-align: 30px;
    color: var(--white);
  }
  .launch__chevrons { width: 108px; height: 56px; flex: none; }
  .handle {
    position: absolute;
    top: 1076px;
    left: 866px;
    width: 284px;
    height: 46px;
    box-sizing: border-box;
    border: 2px solid var(--white);
    border-radius: 23px;
    display: flex;
    align-items: center;
    justify-content: center;
    gap: 12px;
    font-style: italic;
    font-weight: 800;
    font-size: 30px;
    color: var(--white);
    letter-spacing: 1px;
  }
  .handle__dot {
    width: 16px;
    height: 16px;
    border-radius: 50%;
    background: var(--sun);
  }
</style>
</head>
<body>
<main class="ad">
  <svg class="ad__photo" viewBox="0 0 1200 1200" role="img" aria-label="Photo of a woman in black sportswear lifting a slam ball overhead in a gym lit with yellow light, with a blurred battle rope in the foreground">
    <defs>
      <linearGradient id="photoTone" x1="0" y1="0" x2="0.5" y2="1">
        <stop offset="0" stop-color="#f8d21a"/>
        <stop offset="0.5" stop-color="#f2b400"/>
        <stop offset="1" stop-color="#8a6410"/>
      </linearGradient>
      <radialGradient id="figureShade" cx="230" cy="640" r="420" gradientUnits="userSpaceOnUse">
        <stop offset="0" stop-color="#15120c" stop-opacity="0.85"/>
        <stop offset="0.55" stop-color="#2a2010" stop-opacity="0.55"/>
        <stop offset="1" stop-color="#2a2010" stop-opacity="0"/>
      </radialGradient>
      <radialGradient id="ballShade" cx="390" cy="230" r="150" gradientUnits="userSpaceOnUse">
        <stop offset="0" stop-color="#121212" stop-opacity="0.8"/>
        <stop offset="1" stop-color="#121212" stop-opacity="0"/>
      </radialGradient>
      <radialGradient id="ropeBlur" cx="90" cy="1080" r="340" gradientUnits="userSpaceOnUse">
        <stop offset="0" stop-color="#0d0d0d" stop-opacity="0.95"/>
        <stop offset="1" stop-color="#0d0d0d" stop-opacity="0"/>
      </radialGradient>
      <radialGradient id="flare" cx="330" cy="490" r="120" gradientUnits="userSpaceOnUse">
        <stop offset="0" stop-color="#fff6cf" stop-opacity="0.7"/>
        <stop offset="1" stop-color="#fff6cf" stop-opacity="0"/>
      </radialGradient>
      <clipPath id="photoEdge">
        <polygon points="0,0 612,0 598,60 606,120 584,190 592,260 560,333 572,400 538,470 546,540 506,610 512,667 470,740 474,810 430,880 436,940 392,1000 398,1070 352,1130 360,1200 0,1200"/>
      </clipPath>
    </defs>
    <g clip-path="url(#photoEdge)">
      <rect width="620" height="1200" fill="url(#photoTone)"/>
      <rect width="620" height="1200" fill="url(#figureShade)"/>
      <rect width="620" height="1200" fill="url(#ballShade)"/>
      <rect width="620" height="1200" fill="url(#flare)"/>
      <rect width="620" height="1200" fill="url(#ropeBlur)"/>
    </g>
  </svg>

  <header class="brand">
    <span class="brand__name">PulseForge</span>
    <span class="brand__tagline">
      <span class="brand__rule"></span>PERSONAL GROUP TRAINING<span class="brand__rule"></span>
    </span>
  </header>

  <h1 class="headline">
    <span class="headline__line">Bright</span>
    <span class="headline__line">Parent</span>
    <span class="headline__line">Reboot</span>
  </h1>

  <section class="launch">
    <span class="launch__label">Starting</span>
    <div class="launch__row">
      <svg class="launch__chevrons" viewBox="0 0 108 56" aria-hidden="true">
        <polygon fill="#ffffff" points="0,6 24,6 50,28 24,50 0,50 26,28"/>
        <polygon fill="#ffffff" points="52,6 76,6 102,28 76,50 52,50 78,28"/>
      </svg>
      <span class="launch__date">SEPTEMBER 23<sup>Rd</sup></span>
      <svg class="launch__chevrons" viewBox="0 0 108 56" aria-hidden="true">
        <polygon fill="#ffffff" points="108,6 84,6 58,28 84,50 108,50 82,28"/>
        <polygon fill="#ffffff" points="56,6 32,6 6,28 32,50 56,50 30,28"/>
      </svg>
    </div>
  </section>

  <footer class="handle">
    <span class="handle__dot"></span>@PULSEFORGE
  </footer>
</main>
</body>
</html>
```